Employees at R&T Gale Power Services need new modern business cards

We need new business cards that showcase our new rebranded logo. We are seeking modern, clean, fresh, attractive cards while still being professional. We want to stand out. A little bit about us: we work in Canada and the USA. We offer Technical Field Advisors to support wind turbine manufacturers through the construction phase of wind farms. I am attaching a mock inspiration picture to lead you in the direction we want to see this go. Also, FYI We have approx. 10/11 different employees that would need their own card. Let me know when you would need everyone's name. We would love to see some black and white options as well as color copies- when using colors we want green to be the dominant color with accents for blue and orange (colors should match our logo). I have also attached copies of our old business card for reference.

Contact Information for Business Card

Name, Telephone, Email, address, company name, website. EXAMPLE: Dean Whitlock, DeanWhitlock@randtgale.net, 555-384-9162, 318276 Fallow Line #7, Marrowby, ON X9Z 4Q2, www.randtgale.net

Colors
0054AA
0677BA
7BADD7
CADEEF
E8F1F8
00AB8E
00BBA5
67D7C9
C6EFE9
E9F9F6
F0912C
F2A743
F7CA91
FBE8D2
FDF5EE

Requirements
Must have
• 2 sided business card

```html
<!DOCTYPE html>
<html lang="en">
<head>
<meta charset="utf-8">
<title>R&amp;T Gale Power Services – Business Card</title>
<link href="https://fonts.googleapis.com/css2?family=Roboto:wght@400;500&display=swap" rel="stylesheet">
<style>
  :root {
    --page: #ececec;
    --card: #212121;
    --green: #3cb54a;
    --blue: #1a8ad8;
    --blue-deep: #0677ba;
    --orange: #f0912c;
    --amber: #f9b820;
    --ink-light: #e6e6e6;
    --shadow: rgba(0,0,0,0.18);
  }
  * { margin: 0; padding: 0; box-sizing: border-box; }
  html, body { width: 1200px; height: 1200px; overflow: hidden; }
  body {
    background: var(--page);
    font-family: "Roboto", Arial, sans-serif;
    position: relative;
  }
  .card {
    position: absolute;
    left: 281px;
    width: 639px;
    height: 366px;
    background: var(--card);
    border-radius: 20px;
    overflow: hidden;
    box-shadow: 0 4px 14px var(--shadow);
  }
  .card--front { top: 195px; }
  .card--back { top: 639px; }

  .card__art {
    position: absolute;
    inset: 0;
    width: 639px;
    height: 366px;
  }

  .brand-mark {
    position: absolute;
    left: 299px;
    top: 52px;
    width: 300px;
    text-align: center;
  }
  .brand-mark__dot {
    display: block;
    width: 164px;
    height: 164px;
    margin: 0 auto 26px;
    border-radius: 50%;
    background: var(--green);
  }
  .brand-mark__name {
    color: var(--green);
    font-weight: 500;
    font-size: 36px;
    line-height: 1;
    letter-spacing: 3px;
    text-transform: uppercase;
  }

  .holder {
    position: absolute;
    left: 46px;
    top: 124px;
  }
  .holder__name {
    color: var(--green);
    font-weight: 500;
    font-size: 29px;
    letter-spacing: -0.5px;
    text-transform: uppercase;
    line-height: 1;
  }
  .holder__title {
    color: var(--blue);
    font-size: 16.5px;
    margin-top: 6px;
  }
  .contact {
    list-style: none;
    position: absolute;
    left: 46px;
    color: var(--ink-light);
    font-size: 15.5px;
    line-height: 18px;
  }
  .contact--address { top: 203px; }
  .contact--lines { top: 269px; }
  .contact li { position: relative; padding-left: 20px; }
  .contact svg {
    position: absolute;
    left: 0;
    top: 3px;
    width: 11px;
    height: 12px;
    fill: var(--blue);
  }

  .back-brand {
    position: absolute;
    left: 0; right: 0;
    top: 72px;
    text-align: center;
  }
  .back-brand__dot {
    display: block;
    width: 146px;
    height: 146px;
    margin: 0 auto 26px;
    border-radius: 50%;
    background: var(--green);
  }
  .back-brand__name {
    color: var(--green);
    font-weight: 500;
    font-size: 27px;
    line-height: 1;
    letter-spacing: 4px;
    text-transform: uppercase;
  }
</style>
</head>
<body>

<section class="card card--front">
  <svg class="card__art" viewBox="0 0 639 366" aria-hidden="true">
    <defs>
      <linearGradient id="cornerWarm" x1="0" y1="0" x2="0" y2="1">
        <stop offset="0" stop-color="#f9b820"/>
        <stop offset="1" stop-color="#f0912c"/>
      </linearGradient>
      <linearGradient id="cornerCool" x1="0" y1="0" x2="0" y2="1">
        <stop offset="0" stop-color="#1a8ad8"/>
        <stop offset="1" stop-color="#0677ba"/>
      </linearGradient>
    </defs>
    <rect x="500" y="0" width="139" height="183" fill="url(#cornerWarm)"/>
    <rect x="500" y="183" width="139" height="183" fill="url(#cornerCool)"/>
    <circle cx="449" cy="185" r="193" fill="#212121"/>
  </svg>

  <div class="brand-mark">
    <span class="brand-mark__dot"></span>
    <p class="brand-mark__name">R&amp;T Gale</p>
  </div>

  <div class="holder">
    <h1 class="holder__name">Dean Whitlock</h1>
    <p class="holder__title">Owner &amp; CEO</p>
  </div>

  <ul class="contact contact--address">
    <li>
      <svg viewBox="0 0 10 12"><path d="M5 0a4 4 0 0 0-4 4c0 3 4 8 4 8s4-5 4-8a4 4 0 0 0-4-4zm0 5.6A1.6 1.6 0 1 1 5 2.4a1.6 1.6 0 0 1 0 3.2z"/></svg>
      R&amp;T Gale Power Services
    </li>
    <li>318276 Fallow Line #7</li>
    <li>Marrowby, ON X9Z 4Q2</li>
  </ul>

  <ul class="contact contact--lines">
    <li>
      <svg viewBox="0 0 12 12"><path d="M2.5 0.5l2 2.6-1.2 1.4c.7 1.6 2 2.9 3.6 3.6l1.4-1.2 2.6 2-1.2 2.1C5.4 11 1 6.6.4 2z"/></svg>
      555-384-9162
    </li>
    <li>
      <svg viewBox="0 0 12 12"><path d="M0 2.5h12v7H0zM.8 3.2 6 7l5.2-3.8" stroke="#212121" stroke-width="0.8"/></svg>
      DeanWhitlock@randtgale.net
    </li>
    <li>
      <svg viewBox="0 0 12 12"><circle cx="6" cy="6" r="5.5"/><path d="M3 3.5c1.5 0 2 1 1.5 2s1 1.5 1 3M7.5 1.5c0 1.5 1.5 1.5 2.5 2" stroke="#212121" stroke-width="0.9" fill="none"/></svg>
      www.randtgale.net
    </li>
  </ul>
</section>

<section class="card card--back">
  <div class="back-brand">
    <span class="back-brand__dot"></span>
    <p class="back-brand__name">R&amp;T Gale Power Services</p>
  </div>
</section>

</body>
</html>
```